Joomla Responsive Website Template for an International Biotechnology Company

Our client is a biotechnology company that uses silver-based technology to help make products antimicrobial, antibacterial, and anti fungal. We need a Joomla-based template that is responsive/mobile friendly when viewed on tablets or smartphones. We are looking for a template design for the home page and subpages. We are replacing the current website http://www.velmora-labs.com with a new website being built here: http://velmoraclean.com.stagehost.com/velmoraprime/. What we have now on the site is the basic wire frame. This is the desired layout and pictures we want to use. We would like you to add some design elements to make the website more professional looking and polished. Please refer to the attached style guide to help you in choosing the color. The client does like the green leaf, which is included in the last page of style guide and may be good for a background image. While the Velmora logo and leaf are green, we do not want to overuse the color green. The client does own other technologies that we will be promoting on the site and the logos for these technologies are attached below. These logos are Tusk, Velmora-Prime, and Pivn. We will be using this website to promote the technologies, the markets the technologies serve; drinking water, medical devices, apparel and textiles, and architectural surfaces, and to promote the customer using these devices. Please make the design "clean" and not cluttered, as these technologies are used to fight "dirty things".
Updates

Hello Designers! Thank you all very much for your design submissions. They were simply excellent. Due to the Holidays and New Years, many of the client's team members have been on vacation. We expect to have feedback shortly and pick the top design soon there after. Again, thank you all very much and hope the New Year brings you continued success. Best, Dorian

Industry/Entity Type

Biotechnology

Coding

Coded - Design and coding required

```html
<!DOCTYPE html>
<html lang="en">
<head>
<meta charset="utf-8">
<title>Velmora – Keeping the world's surface safe</title>
<link href="https://fonts.googleapis.com/css2?family=Raleway:wght@400;500;600;700&family=Open+Sans:wght@400;600&display=swap" rel="stylesheet">
<style>
  :root {
    --green: #6ab42d;
    --ink: #333333;
    --text: #666666;
    --muted: #888888;
    --line: #e2e2e2;
    --white: #ffffff;
    --slate: #4a5563;
    --footer: #4b4b4d;
    --footer-text: #c9c9c9;
    --search: #8a8a8a;
  }
  * { box-sizing: border-box; margin: 0; padding: 0; }
  html, body { width: 958px; height: 1200px; overflow: hidden; background: var(--white); }
  body { font-family: "Raleway", sans-serif; color: var(--text); position: relative; }
  .page { position: relative; width: 958px; height: 1200px; overflow: hidden; }

  /* header */
  .brand { position: absolute; left: 106px; top: 27px; display: flex; align-items: center; gap: 9px;
    font-weight: 600; font-size: 30px; line-height: 36px; color: var(--green); }
  .brand .mark { width: 14px; height: 14px; background: var(--green); display: block; }
  .social-top { position: absolute; left: 681px; top: 38px; display: flex; gap: 6px; }
  .social-top span { width: 25px; height: 25px; border-radius: 50%; display: block; }
  .s1 { background: #1b75bb; } .s2 { background: #2aa3e0; } .s3 { background: #f5a623; } .s4 { background: #d0422f; }
  .search { position: absolute; left: 821px; top: 36px; width: 32px; height: 29px; background: var(--search); }
  .search svg { position: absolute; left: 10px; top: 8px; }

  .nav { position: absolute; left: 0; top: 92px; width: 958px; height: 47px; border-top: 1px solid var(--line);
    box-shadow: 0 2px 3px rgba(0,0,0,.06); }
  .nav a { position: absolute; top: 10px; font-size: 12px; color: var(--ink); text-decoration: none; line-height: 29px; }
  .nav a.active { left: 107px; width: 59px; background: var(--green); color: var(--white); text-align: center; font-weight: 500; }

  /* hero */
  .hero { position: absolute; left: 0; top: 139px; width: 958px; height: 387px;
    background: radial-gradient(ellipse 260px 90px at 620px 270px, #1c3f7a 0%, #3a66a8 45%, transparent 100%),
                linear-gradient(180deg, #bfe0f0 0%, #8fbde0 35%, #5f8fcb 70%, #6a96cf 100%); }
  .hero-title { position: absolute; left: 104px; top: 131px; }
  .hero-title span { display: block; width: max-content; background: var(--slate); color: var(--white);
    font-size: 29px; font-weight: 500; padding: 0 13px 0 16px; line-height: 35px; margin-bottom: 6px; }
  .hero-text { position: absolute; left: 106px; top: 228px; font-size: 12.5px; line-height: 22px; color: #2d3440; font-weight: 500; }
  .dots { position: absolute; left: 436px; top: 350px; width: 86px; height: 23px; background: #3f4a5c; border-radius: 2px;
    display: flex; justify-content: center; align-items: center; gap: 6px; }
  .dots i { width: 10px; height: 10px; border-radius: 50%; background: var(--white); display: block; }
  .dots i.on { background: var(--green); }

  /* partner brands */
  .partners { position: absolute; left: 103px; top: 560px; display: flex; gap: 15px; }
  .partner { width: 113px; height: 62px; border: 1px solid #cfcfcf; display: flex; align-items: center; justify-content: center;
    font-size: 21px; font-weight: 700; color: var(--ink); }

  /* markets */
  .markets { position: absolute; left: 104px; top: 674px; display: flex; gap: 16px; }
  .market { width: 176px; text-align: center; }
  .market .photo { width: 176px; height: 107px; }
  .market h3 { font-size: 15px; font-weight: 500; color: var(--green); margin-top: 17px; }
  .p-water { background: linear-gradient(160deg, #2a5a8a, #0f2d52); }
  .p-medical { background: linear-gradient(160deg, #dfe7ee, #6b9cc6); }
  .p-textile { background: linear-gradient(180deg, #555 0%, #3a3a3a 40%, #2e3550 75%, #244b8c 100%); }
  .p-arch { background: linear-gradient(160deg, #efefef, #c9c5bd); }

  .rule { position: absolute; left: 104px; top: 844px; width: 751px; height: 1px; background: var(--line); }

  /* about */
  .about { position: absolute; left: 105px; top: 876px; width: 485px; }
  .about h2 { font-size: 20px; font-weight: 500; color: var(--ink); }
  .about p { font-size: 10.5px; line-height: 19px; color: var(--text); margin-top: 20px; }
  .col-rule { position: absolute; left: 598px; top: 875px; width: 1px; height: 184px; background: var(--line); }

  .news { position: absolute; left: 615px; top: 873px; width: 260px; }
  .news h2 { font-size: 20px; font-weight: 500; color: var(--ink); }
  .news .arrows { position: absolute; left: 220px; top: 6px; }
  .story { position: absolute; left: 2px; display: flex; gap: 17px; width: 260px; }
  .story .thumb { width: 78px; height: 53px; flex: none; }
  .story p { font-size: 10.5px; line-height: 17.5px; color: var(--muted); }
  .t1 { background: linear-gradient(135deg, #d9c8a0, #8a6a52); }
  .t2 { background: linear-gradient(135deg, #e8d8e0, #6fb4cc); }

  /* footer */
  .footer { position: absolute; left: 0; top: 1110px; width: 958px; height: 90px; background: var(--footer); }
  .footer nav { position: absolute; left: 105px; top: 24px; font-size: 10px; }
  .footer nav a { color: var(--footer-text); text-decoration: none; margin-right: 11px; }
  .copy { position: absolute; left: 106px; top: 52px; font-family: "Open Sans", sans-serif; font-size: 10px; color: var(--white); }
  .follow { position: absolute; left: 719px; top: 21px; font-size: 11.5px; color: var(--white); }
  .social-foot { position: absolute; left: 715px; top: 46px; display: flex; gap: 5px; }
  .social-foot span { width: 24px; height: 24px; border-radius: 50%; background: var(--white); display: block; }
</style>
</head>
<body>
<div class="page">
  <header>
    <div class="brand"><span class="mark"></span>Velmora</div>
    <div class="social-top" aria-label="Social links"><span class="s1"></span><span class="s2"></span><span class="s3"></span><span class="s4"></span></div>
    <div class="search" aria-label="Search">
      <svg width="12" height="12" viewBox="0 0 12 12"><circle cx="5" cy="5" r="3.5" fill="none" stroke="#fff" stroke-width="1.6"/><line x1="7.6" y1="7.6" x2="10.5" y2="10.5" stroke="#fff" stroke-width="1.8"/></svg>
    </div>
    <nav class="nav">
      <a class="active" href="#">Home</a>
      <a href="#" style="left:198px">About Us</a>
      <a href="#" style="left:292px">Markets</a>
      <a href="#" style="left:372px">Technology</a>
      <a href="#" style="left:484px">Customer Programs</a>
      <a href="#" style="left:637px">News Highlights</a>
      <a href="#" style="left:771px">Contact Us</a>
    </nav>
  </header>

  <section class="hero" role="img" aria-label="Water droplet falling into a blue pool with rippling rings">
    <h1 class="hero-title"><span>Keeping the world’s</span><span>Surface safe..</span></h1>
    <p class="hero-text">Neque porro quisquam est qui dolorem ipsum quia<br>dolor sit amet, consectetur, adipisci velit.</p>
    <div class="dots"><i class="on"></i><i></i><i></i><i></i></div>
  </section>

  <section class="partners">
    <div class="partner" style="color:#1f7fc0">Pivn</div>
    <div class="partner" style="color:#d83a2e">Tusk</div>
    <div class="partner">Prime</div>
    <div class="partner" style="color:#1d4f9a">Medalio</div>
    <div class="partner">Ebrix</div>
    <div class="partner" style="font-size:15px">Dr. Fenwick</div>
  </section>

  <section class="markets">
    <div class="market"><div class="photo p-water" role="img" aria-label="Water filter pitcher"></div><h3>Drinking Water</h3></div>
    <div class="market"><div class="photo p-medical" role="img" aria-label="Nurse adjusting a hospital monitor beside a patient"></div><h3>Medical Devices</h3></div>
    <div class="market"><div class="photo p-textile" role="img" aria-label="Stack of folded fabrics"></div><h3>Apparel &amp; Textiles</h3></div>
    <div class="market"><div class="photo p-arch" role="img" aria-label="Laboratory benches with equipment"></div><h3>Architectural Surfaces</h3></div>
  </section>

  <div class="rule"></div>

  <section class="about">
    <h2>Velmora® Antimicrobial</h2>
    <p>Velmora branded antimicrobial technology makes products cleaner and longer lasting with silver, copper and zinc, which have been proven in use throughout history. Velmora antimicrobial technology provides built-in protection by working 24/7 resisting the growth of microbes. We work in close partnership with our customers, from development to end-user marketing, to deliver a product advantage that makes a real difference in the marketplace.</p>
    <p>*Velmora is a Federal Registry listed ionic silver technology and is not a nanosilver technology.</p>
  </section>
  <div class="col-rule"></div>

  <section class="news">
    <h2>News &amp; Events</h2>
    <svg class="arrows" width="20" height="12" viewBox="0 0 20 12"><polyline points="6,1 1,6 6,11" fill="none" stroke="#666" stroke-width="1.6"/><polyline points="14,1 19,6 14,11" fill="none" stroke="#aaa" stroke-width="1.6"/></svg>
    <div class="story" style="top:43px"><div class="thumb t1" role="img" aria-label="Portrait of a man outdoors"></div><p>Larkin’s Chooses Velmora Prime to Deliver Odor Elimination Benefits.</p></div>
    <div class="story" style="top:121px"><div class="thumb t2" role="img" aria-label="Mother and daughter shopping"></div><p>Harborview Marathon Winner Wears Stridewell Shoes Protected by Velmora Antimicrobial</p></div>
  </section>

  <footer class="footer">
    <nav><a href="#">Home</a><a href="#">About Us</a><a href="#">Markets</a><a href="#">Technology</a><a href="#">Customer Programs</a><a href="#">News Highlights</a><a href="#">Contact Us</a></nav>
    <p class="copy">Copyright © 2014 Yoursite. All rights reserved.</p>
    <p class="follow">Follow Us</p>
    <div class="social-foot" aria-label="Social links"><span></span><span></span><span></span><span></span><span></span></div>
  </footer>
</div>
</body>
</html>
```